Colocation Data Center Web Site

Would be to design a specialized site specifically for a Data Center that provide colocation services to their clients.
This site would need to have a client portal to allow them to see the status of their bills, list of services and to create service tickets.

Industry/Entity Type

It Service

```html
<!DOCTYPE html>
<html lang="en">
<head>
<meta charset="utf-8">
<title>Kestrelhost – Dedicated Servers</title>
<link href="https://fonts.googleapis.com/css2?family=Open+Sans:wght@400;600&family=PT+Sans+Narrow:wght@400;700&display=swap" rel="stylesheet">
<style>
  :root {
    --navy: #3f4470;
    --navy-band: #4a4f7c;
    --button: #4b5183;
    --text-dark: #454545;
    --text-body: #555555;
    --hero-bg: #eeeef8;
    --header-top: #ffffff;
    --header-bottom: #e9e9ec;
    --rule: #d4d4da;
    --accent-line: #5a6096;
    --server-light: #3c3c3c;
    --server-dark: #121212;
    --white: #ffffff;
  }
  * { box-sizing: border-box; margin: 0; padding: 0; }
  html, body { width: 1200px; height: 900px; overflow: hidden; }
  body {
    position: relative;
    font-family: "Open Sans", sans-serif;
    background: var(--white);
    color: var(--text-body);
  }

  /* Top utility bar */
  .utility-bar {
    position: absolute; top: 0; left: 0; width: 1200px; height: 32px;
    background: var(--navy); color: var(--white);
    font-family: "PT Sans Narrow", sans-serif; font-size: 15px;
  }
  .utility-left { position: absolute; left: 93px; top: 6px; display: flex; align-items: center; gap: 8px; }
  .utility-left .divider { margin: 0 4px; }
  .utility-right { position: absolute; right: 107px; top: 7px; display: flex; gap: 16px; font-size: 13px; }
  .social-link { display: flex; align-items: center; gap: 6px; }
  .social-link .chip { width: 18px; height: 18px; background: var(--white); display: inline-block; }

  /* Header */
  .site-header {
    position: absolute; top: 32px; left: 0; width: 1200px; height: 98px;
    background: linear-gradient(var(--header-top), var(--header-bottom));
    border-bottom: 1px solid var(--rule);
  }
  .brand { position: absolute; left: 93px; top: 22px; display: flex; flex-direction: column; align-items: flex-start; gap: 8px; }
  .brand .mark { width: 30px; height: 30px; border-radius: 50%; background: var(--navy); margin-left: 24px; }
  .brand .name { font-size: 11px; letter-spacing: 3px; color: var(--navy); font-weight: 600; }

  .main-nav { position: absolute; right: 107px; top: 0; height: 98px; display: flex; font-family: "PT Sans Narrow", sans-serif; font-size: 17px; color: var(--text-dark); }
  .nav-item { position: relative; height: 98px; padding: 29px 9px 0; display: flex; flex-direction: column; align-items: center; gap: 12px; border-left: 1px solid var(--rule); }
  .nav-item:first-child { border-left: none; }
  .nav-item svg { width: 22px; height: 22px; fill: #555; }
  .nav-item.active::after { content: ""; position: absolute; left: 4px; right: 4px; bottom: 0; height: 3px; background: var(--accent-line); }

  /* Hero */
  .hero { position: absolute; top: 131px; left: 0; width: 1200px; height: 494px; background: radial-gradient(circle at 850px 250px, #f8f8fd, var(--hero-bg) 60%); }
  .hero-title { position: absolute; left: 93px; top: 53px; font-family: "PT Sans Narrow", sans-serif; font-weight: 700; font-size: 56px; line-height: 1; color: var(--text-dark); letter-spacing: -0.5px; }
  .hero-subtitle { position: absolute; left: 93px; top: 110px; font-family: "PT Sans Narrow", sans-serif; font-size: 29px; line-height: 1; color: var(--text-dark); }
  .hero-intro { position: absolute; left: 93px; top: 165px; width: 430px; font-size: 16px; line-height: 21px; color: var(--text-body); }
  .feature-list { position: absolute; left: 93px; top: 237px; list-style: none; font-size: 14.5px; color: var(--text-body); }
  .feature-list li { display: flex; align-items: center; gap: 10px; height: 20px; }
  .feature-list li + li { margin-top: 18px; }
  .feature-list li:last-child { margin-top: 23px; }
  .radio { width: 19px; height: 19px; border-radius: 50%; border: 2px solid #c9cad8; background: #e8e8f0; }
  .radio.checked { background: radial-gradient(circle, #aeb0cc 45%, #e8e8f0 50%); }
  .hero-actions { position: absolute; left: 93px; top: 420px; display: flex; gap: 38px; }
  .button { width: 133px; height: 38px; background: var(--button); color: var(--white); border: 1px solid #2f3358; border-radius: 4px; font-family: "PT Sans Narrow", sans-serif; font-size: 22px; display: flex; align-items: center; justify-content: center; box-shadow: 0 2px 3px rgba(0,0,0,0.25); }
  .hero-visual { position: absolute; left: 660px; top: 50px; width: 390px; height: 370px; border-radius: 16px; background: linear-gradient(135deg, var(--server-light), var(--server-dark)); box-shadow: 0 20px 40px rgba(60,64,110,0.25); }

  /* Statement band */
  .statement-band { position: absolute; top: 625px; left: 0; width: 1200px; height: 100px; background: var(--navy-band); color: var(--white); font-family: "PT Sans Narrow", sans-serif; font-size: 19.5px; line-height: 28px; text-align: center; padding-top: 23px; text-transform: uppercase; }
  .band-shadow { position: absolute; top: 725px; left: 100px; width: 1000px; height: 20px; background: radial-gradient(ellipse at 50% 0, rgba(0,0,0,0.18), transparent 70%); }

  /* Product row */
  .product-visual { position: absolute; top: 770px; height: 130px; }
  .product-visual.one { left: 115px; width: 205px; background: linear-gradient(#4a4f55, #1e2024); border-radius: 30px 30px 0 0; }
  .product-visual.two { left: 378px; width: 175px; background: linear-gradient(#333, #111); }
  .product-visual.three { left: 640px; width: 152px; background: linear-gradient(#d9dadd, #6a6c70); border-radius: 10px 10px 40px 40px; }
  .product-visual.four { left: 855px; width: 195px; top: 818px; height: 82px; background: linear-gradient(#9a9ea4, #4d5156); }
</style>
</head>
<body>

<div class="utility-bar">
  <div class="utility-left">
    <span>Privacy Policy</span><span class="divider">|</span>
    <svg width="26" height="22" viewBox="0 0 26 22" aria-hidden="true"><circle cx="8" cy="6" r="4.5" fill="#fff"/><path d="M0 21c0-6 4-9 8-9s8 3 8 9z" fill="#fff"/><circle cx="18" cy="6" r="4" fill="#fff"/><path d="M12 21c1-5 3-8 7-8 4 0 7 3 7 8z" fill="#fff"/></svg>
    <span>Live Chat</span>
  </div>
  <div class="utility-right">
    <span class="social-link"><span class="chip"></span>Circles</span>
    <span class="social-link"><span class="chip"></span>Chirper</span>
    <span class="social-link"><span class="chip"></span>ProLink</span>
    <span class="social-link"><span class="chip"></span>FaceSpace</span>
  </div>
</div>

<header class="site-header">
  <div class="brand">
    <span class="mark"></span>
    <span class="name">KESTRELHOST</span>
  </div>
  <nav class="main-nav">
    <div class="nav-item active"><svg viewBox="0 0 24 24"><path d="M12 3 2 12h3v9h5v-6h4v6h5v-9h3z"/></svg>Home</div>
    <div class="nav-item"><svg viewBox="0 0 24 24" fill="none" stroke="#555" stroke-width="1.5"><circle cx="12" cy="12" r="8"/><path d="M4 12h16M12 4c-4 4-4 12 0 16M12 4c4 4 4 12 0 16"/></svg>Web Hosting</div>
    <div class="nav-item"><svg viewBox="0 0 24 24" fill="none" stroke="#555" stroke-width="2"><circle cx="8" cy="9" r="4"/><circle cx="17" cy="14" r="3.5"/></svg>Features</div>
    <div class="nav-item"><svg viewBox="0 0 24 24" fill="none" stroke="#555" stroke-width="2"><circle cx="8" cy="9" r="4"/><circle cx="17" cy="14" r="3.5"/></svg>Services</div>
    <div class="nav-item"><svg viewBox="0 0 24 24" fill="none" stroke="#555" stroke-width="2"><circle cx="8" cy="9" r="4"/><circle cx="17" cy="14" r="3.5"/></svg>Blog</div>
    <div class="nav-item"><svg viewBox="0 0 24 24"><circle cx="12" cy="7" r="5"/><path d="M4 22c0-7 4-9 8-9s8 2 8 9z"/></svg>Support</div>
    <div class="nav-item"><svg viewBox="0 0 24 24"><path d="M2 10c0-3 5-5 10-5s10 2 10 5l-4 1-1-3H7L6 11z"/><circle cx="12" cy="14" r="3.5"/></svg>Contact</div>
  </nav>
</header>

<section class="hero">
  <h1 class="hero-title">DEDICATED SERVERS</h1>
  <p class="hero-subtitle">SIMPLY DUMMY TEXT FOR PRINTING TYPE</p>
  <p class="hero-intro">Internet tend to repeat predefined chunks as necessary making this the first true generator on the internet.</p>
  <ul class="feature-list">
    <li><span class="radio checked"></span>Unlimited Bandwidth with Massive Storage</li>
    <li><span class="radio"></span>Unlimited Bandwidth with Massive Storage</li>
    <li><span class="radio"></span>Unlimited Bandwidth with Massive Storage</li>
    <li><span class="radio"></span>Unlimited Bandwidth with Massive Storage</li>
  </ul>
  <div class="hero-actions">
    <span class="button">VIEW DETAIL</span>
    <span class="button">SIGNUP NOW</span>
  </div>
  <div class="hero-visual" role="img" aria-label="Two black perforated dedicated server towers with green drive bays"></div>
</section>

<div class="statement-band">
  We have registered over 2 million domain names and host over 1.9 million websites for individuals and organizations our<br>
  fast and flexible website creator is the easy way to build &amp; manage a site for your business
</div>
<div class="band-shadow"></div>

<div class="product-visual one" role="img" aria-label="Cloud server stack with blue lights"></div>
<div class="product-visual two" role="img" aria-label="Row of black rack servers"></div>
<div class="product-visual three" role="img" aria-label="Two silver server towers on stacked discs"></div>
<div class="product-visual four" role="img" aria-label="Grey server cabinets in a row"></div>

</body>
</html>
```